AVOID HOT “HARISSA” SAUCE. IN CAN

Brand Overview: Create a dynamic and eye-catching label for our new hot sauce IN CAN, “DUMEL.” Our brand is all about delivering a fiery flavor experience that combines the intensity of various peppers with unique, bold ingredients. The hot sauce targets spice enthusiasts who crave both heat and distinctive taste profiles.

Key Messages: Intensity: Emphasize the extreme heat level of the hot sauce to appeal to spice lovers.
Traditional: The taste is traditional
Flavor Fusion: Highlight the unique blend of peppers and special ingredients that sets DUMEL

Quality Ingredients: Convey the use of premium, natural ingredients to reinforce the high-quality aspect of our product.

Versatility: Communicate the sauce's versatility – perfect for various cuisines and dishes. Design Elements:

Color Palette: Use fiery reds, oranges, and yellows to convey the heat, with accents of dark and smoky tones to suggest depth of flavor.

Typography: Choose bold and legible fonts for the product name, ensuring it is easily readable from a distance.
Imagery: Incorporate visuals of flaming peppers or a stylized fire to reinforce the spicy nature of the hot sauce.
Consider using images of the key ingredients to showcase the fusion of flavors.

Texture/Background: Add a textured or gradient background to enhance visual interest and give a sense of depth.

Label Information: Product Name Hot Sauce "HARISSA" Heat Level

Indicator: Use a visual scale or iconography to indicate the spiciness level.

Ingredients: Highlight key ingredients and emphasize their quality, peppers, water, salt
SIZE: L: 12cm H: 5.5cm

Net Weight: 140g

Regulatory Information: Ensure compliance with all relevant food labeling regulations, including ingredients list, nutritional information, and contact details.

Competitor Analysis: Examine other hot sauce labels in the market to identify design trends and differentiators.
Inspiration: Consider drawing inspiration from elements like flames, peppers, or global spice motifs to create a visually striking and memorable label. Mood/Emotion: The label should evoke excitement, daring, and a sense of adventure – capturing the thrill of experiencing the intense flavor of HARISSA DUMEL Hot Sauce.

Target Audience: Spice enthusiasts, foodies, and individuals seeking a unique and bold addition to their culinary experiences.

Delivery Format: The label design should be suitable for various packaging sizes, ensuring scalability without sacrificing visual impact. Remember to balance the vibrant and intense visuals with clarity and readability and send the FONT at the moment of the delivery.
Updates

Need extra days to review

Target Market(s)

European

Font styles to use
Decorative

Colors
FFF300
FFF600
FEFA6F
FFFEC7
FFFEE8
FFC000
F8CF3A
FAE287
FDF2CF
FEFAEE
EE7325
F08F49
F5BC92
FAE3D3
FDF4ED
EB3D1F
EC4F4E
F09395
F8D3D4
FCEDEE

Requirements
Must have
• LOGO, BARCODE, Nutritional facts, INGREDIENTS

```html
<!DOCTYPE html>
<html lang="en">
<head>
<meta charset="utf-8">
<title>DUMEL Harissa Hot Sauce – Can Label</title>
<link rel="stylesheet" href="https://fonts.googleapis.com/css2?family=Anton&family=Courgette&family=Montserrat:wght@600;700;800&display=swap">
<style>
  :root {
    --backdrop: #e4e4e4;
    --fire-deep: #7a0608;
    --fire-red: #d4121a;
    --fire-orange: #ee7325;
    --fire-yellow: #fff300;
    --fire-amber: #ffc000;
    --ember: #2a0204;
    --drop-red: #a3162a;
    --badge-red: #8c0a0c;
    --chili-red: #b01010;
    --cream: #fffee8;
    --white: #ffffff;
  }
  * { margin: 0; padding: 0; box-sizing: border-box; }
  html, body {
    width: 1200px; height: 1200px; overflow: hidden;
    background: var(--backdrop);
  }
  .label {
    position: absolute; left: 270px; top: 108px;
    width: 660px; height: 985px; overflow: hidden;
    background:
      linear-gradient(90deg, rgba(60,0,0,.25) 0%, rgba(0,0,0,0) 25%, rgba(0,0,0,0) 75%, rgba(80,10,0,.25) 100%),
      linear-gradient(180deg, var(--fire-deep) 0%, var(--fire-red) 30%, var(--fire-red) 48%, var(--fire-orange) 62%, var(--fire-yellow) 76%, var(--fire-amber) 90%, #f0a020 100%);
  }
  .flame-drop-art {
    position: absolute; left: 92px; top: 40px;
    width: 488px; height: 685px;
    border-radius: 45% 45% 50% 50% / 40% 40% 36% 36%;
    background: linear-gradient(180deg, var(--ember) 0%, #3a0508 45%, var(--drop-red) 75%, #5c0610 100%);
  }
  .brand {
    position: absolute; left: 0; width: 660px; top: 318px;
    text-align: center;
    font-family: "Montserrat", sans-serif; font-weight: 800;
    font-size: 82px; letter-spacing: 2px; color: var(--white);
    line-height: 1;
  }
  .product-name {
    position: absolute; left: 0; width: 660px; top: 452px;
    text-align: center; font-weight: 400;
    font-family: "Anton", sans-serif; font-size: 118px;
    letter-spacing: 4px; color: var(--white); line-height: 1;
  }
  .product-type {
    position: absolute; left: 0; width: 660px; top: 572px;
    text-align: center;
    font-family: "Courgette", cursive; font-size: 62px;
    color: var(--white); line-height: 1;
  }
  .ingredients {
    position: absolute; left: 0; width: 660px; top: 731px;
    text-align: center;
    font-family: "Montserrat", sans-serif; font-weight: 700;
    font-size: 19px; line-height: 1.3; color: var(--cream);
  }
  .heat-scale {
    position: absolute; left: 158px; top: 788px;
    width: 356px; height: 72px; display: flex;
    border: 2px solid var(--badge-red);
  }
  .heat-scale .heat-level {
    width: 180px; background: var(--badge-red); color: var(--white);
    font-family: "Montserrat", sans-serif; font-weight: 700; font-size: 23px;
    display: flex; align-items: center; justify-content: center;
  }
  .heat-scale .heat-icons {
    flex: 1; background: var(--white);
    display: flex; align-items: center; justify-content: center;
  }
  .net-weight {
    position: absolute; left: 263px; top: 881px;
    width: 146px; height: 104px; background: var(--badge-red);
    color: var(--white); text-align: center;
    font-family: "Montserrat", sans-serif;
    padding-top: 14px;
  }
  .net-weight .caption { font-size: 16px; font-weight: 700; }
  .net-weight .value { font-size: 34px; font-weight: 800; margin-top: 4px; }
</style>
</head>
<body>
  <main class="label">
    <div class="flame-drop-art" role="img" aria-label="Illustration: a large drop of dark red sauce crowned with flames"></div>

    <div class="brand">DUMEL</div>
    <h1 class="product-name">HARISSA</h1>
    <div class="product-type">Hot Sauce</div>

    <p class="ingredients">MADE WITH QUALITY INGREDIENTS:<br>PEPPERS, WATER, SALT</p>

    <div class="heat-scale">
      <div class="heat-level">EXTRA HOT</div>
      <div class="heat-icons" role="img" aria-label="Heat level 5 of 5">
        <svg width="150" height="40" viewBox="0 0 150 40">
          <g fill="var(--chili-red)">
            <path d="M18 6 C24 8 24 20 16 30 C12 35 6 36 6 34 C12 28 14 20 14 10 Z"/>
            <path d="M46 6 C52 8 52 20 44 30 C40 35 34 36 34 34 C40 28 42 20 42 10 Z"/>
            <path d="M74 6 C80 8 80 20 72 30 C68 35 62 36 62 34 C68 28 70 20 70 10 Z"/>
            <path d="M102 6 C108 8 108 20 100 30 C96 35 90 36 90 34 C96 28 98 20 98 10 Z"/>
            <path d="M130 6 C136 8 136 20 128 30 C124 35 118 36 118 34 C124 28 126 20 126 10 Z"/>
          </g>
        </svg>
      </div>
    </div>

    <div class="net-weight">
      <div class="caption">Net Weight:</div>
      <div class="value">140g</div>
    </div>
  </main>
</body>
</html>
```